Business Card Design Project

We are an incubator company that helps young entrepreneur to launch new ideas into the market. We will be targeting investors or likewise; Angels, young entrepreneurs and technopreneurs.

Our logo is being tasked by artflockly to design, therefore there is no logo for now.
You can us Lanternfold Pte Ltd as the logo for the time being.

Please let us have some versions of modern and yet professional designs; for words, you can indicate e.g (address), (Title)

thanks

Target Market(s)

young entrepreneurs
angels, investors

Industry/Entity Type

Business

Colors
3176b5
ffffff

Requirements
Must have
• able to project out our name; Lanternfold
Should not have
• Nothing childish or cartoon

```html
<!DOCTYPE html>
<html lang="en">
<head>
<meta charset="utf-8">
<title>Lanternfold Pte Ltd — Business Card Variants</title>
<link href="https://fonts.googleapis.com/css2?family=Open+Sans:wght@400;600&display=swap" rel="stylesheet">
<style>
  :root {
    --backdrop: #eeeae6;
    --card: #ffffff;
    --ink: #2b2b2b;
    --rule: #4a4a4a;
    --orange: #e8492a;
    --yellow: #f6b727;
    --teal: #1aaba4;
  }
  * { box-sizing: border-box; margin: 0; padding: 0; }
  html, body {
    width: 1200px; height: 900px; overflow: hidden;
    background: var(--backdrop);
    font-family: "Open Sans", Arial, sans-serif;
    color: var(--ink);
  }
  .card-set { position: relative; width: 1200px; height: 900px; }
  .card {
    position: absolute;
    width: 540px; height: 310px;
    background: var(--card);
    display: flex;
    overflow: hidden;
    box-shadow: 0 10px 24px rgba(0,0,0,.18);
  }
  .card--orange { left: 330px; top: 40px;  --accent: var(--orange); }
  .card--yellow { left: 40px;  top: 410px; --accent: var(--yellow); }
  .card--teal   { left: 620px; top: 470px; --accent: var(--teal); }

  .brand-band {
    position: relative;
    width: 170px; height: 100%;
    background: var(--accent);
    flex-shrink: 0;
  }
  .brand-mark {
    position: absolute;
    left: 14px; bottom: 22px;
    display: flex; align-items: center; gap: 8px;
  }
  .brand-mark__dot {
    width: 22px; height: 22px; border-radius: 50%;
    background: var(--card);
    flex-shrink: 0;
  }
  .brand-mark__name {
    font-size: 17px; font-weight: 600; color: var(--card);
    letter-spacing: .3px;
  }

  .details { flex: 1; padding: 40px 30px 0 24px; }
  .holder__name { font-size: 19px; line-height: 1.1; }
  .holder__role { font-size: 12px; line-height: 1.2; }
  .rule { border: 0; border-top: 1px solid var(--rule); margin: 34px 0 10px; }
  .company__name { font-size: 18px; line-height: 1.2; text-align: center; }
  .company__address { font-size: 12px; line-height: 1.4; text-align: center; }
  .rule--second { margin: 10px 0 14px; }
  .contact { list-style: none; font-size: 13px; line-height: 1.35; }
  .contact li { display: flex; align-items: center; gap: 8px; white-space: nowrap; }
  .contact svg { width: 13px; height: 13px; fill: var(--ink); flex-shrink: 0; }
</style>
</head>
<body>
<main class="card-set">

  <article class="card card--orange">
    <div class="brand-band">
      <div class="brand-mark"><span class="brand-mark__dot"></span><span class="brand-mark__name">Lanternfold</span></div>
    </div>
    <section class="details">
      <p class="holder__name">Your name</p>
      <p class="holder__role">your position</p>
      <hr class="rule">
      <p class="company__name">LANTERNFOLD PTE LTD.</p>
      <p class="company__address">777 Harbour Lane, Eastport 54321</p>
      <hr class="rule rule--second">
      <ul class="contact">
        <li><svg viewBox="0 0 16 16"><path d="M2 5c0-2 3-3 6-3s6 1 6 3v1h-3V5H5v1H2zM3 8h10l1 6H2z"/></svg>+ 000 - 4821 - 3907</li>
        <li><svg viewBox="0 0 16 16"><path d="M4 1h8v4H4zM1 6h14v6h-3v3H4v-3H1zm4 4v4h6v-4z"/></svg>+ 000 - 6153 - 2284</li>
        <li><svg viewBox="0 0 16 16"><path d="M1 3h14v10H1zm1.5 1.5L8 9l5.5-4.5z"/></svg>admin@lanternfold.com</li>
        <li><svg viewBox="0 0 16 16"><path d="M1 2h14v9H1zm1.5 1.5v6h11v-6zM6 12h4v1.5h2V15H4v-1.5h2z"/></svg>lanternfold.com</li>
      </ul>
    </section>
  </article>

  <article class="card card--yellow">
    <div class="brand-band">
      <div class="brand-mark"><span class="brand-mark__dot"></span><span class="brand-mark__name">Lanternfold</span></div>
    </div>
    <section class="details">
      <p class="holder__name">Your name</p>
      <p class="holder__role">your position</p>
      <hr class="rule">
      <p class="company__name">LANTERNFOLD PTE LTD.</p>
      <p class="company__address">777 Harbour Lane, Eastport 54321</p>
      <hr class="rule rule--second">
      <ul class="contact">
        <li><svg viewBox="0 0 16 16"><path d="M2 5c0-2 3-3 6-3s6 1 6 3v1h-3V5H5v1H2zM3 8h10l1 6H2z"/></svg>+ 000 - 4821 - 3907</li>
        <li><svg viewBox="0 0 16 16"><path d="M4 1h8v4H4zM1 6h14v6h-3v3H4v-3H1zm4 4v4h6v-4z"/></svg>+ 000 - 6153 - 2284</li>
        <li><svg viewBox="0 0 16 16"><path d="M1 3h14v10H1zm1.5 1.5L8 9l5.5-4.5z"/></svg>admin@lanternfold.com</li>
        <li><svg viewBox="0 0 16 16"><path d="M1 2h14v9H1zm1.5 1.5v6h11v-6zM6 12h4v1.5h2V15H4v-1.5h2z"/></svg>lanternfold.com</li>
      </ul>
    </section>
  </article>

  <article class="card card--teal">
    <div class="brand-band">
      <div class="brand-mark"><span class="brand-mark__dot"></span><span class="brand-mark__name">Lanternfold</span></div>
    </div>
    <section class="details">
      <p class="holder__name">Your name</p>
      <p class="holder__role">your position</p>
      <hr class="rule">
      <p class="company__name">LANTERNFOLD PTE LTD.</p>
      <p class="company__address">777 Harbour Lane, Eastport 54321</p>
      <hr class="rule rule--second">
      <ul class="contact">
        <li><svg viewBox="0 0 16 16"><path d="M2 5c0-2 3-3 6-3s6 1 6 3v1h-3V5H5v1H2zM3 8h10l1 6H2z"/></svg>+ 000 - 4821 - 3907</li>
        <li><svg viewBox="0 0 16 16"><path d="M4 1h8v4H4zM1 6h14v6h-3v3H4v-3H1zm4 4v4h6v-4z"/></svg>+ 000 - 6153 - 2284</li>
        <li><svg viewBox="0 0 16 16"><path d="M1 3h14v10H1zm1.5 1.5L8 9l5.5-4.5z"/></svg>admin@lanternfold.com</li>
        <li><svg viewBox="0 0 16 16"><path d="M1 2h14v9H1zm1.5 1.5v6h11v-6zM6 12h4v1.5h2V15H4v-1.5h2z"/></svg>lanternfold.com</li>
      </ul>
    </section>
  </article>

</main>
</body>
</html>
```